Wordpress theme website for professionals working together

My partner and I are offering business services, my wife in the energy business as mainly as member of the board of commissioners. I am working as interim manager/consultant in the accounting and finance area. Both activities are connected in one company OLVEN BV (dutch ltd). We need a CV based website. Beside this we do some financial and accounting services.

Target Market(s)

small medium business

Font styles to use
Sans Serif

Colors

Designer to choose colors to be used in the design.

Requirements
Must have
• Pictures of both members.
• CLEAN AND SIMPLE
• I LIKE BLACK & WHITE
Nice to have
• I like design like this theme: http://theme.plinterbex.com/resume/

```html
<!DOCTYPE html>
<html lang="en">
<head>
<meta charset="utf-8">
<title>OLVEN BV — Pieter &amp; Marleen</title>
<link href="https://fonts.googleapis.com/css2?family=Montserrat:wght@400;500;600;700&family=Lato:wght@400;700&display=swap" rel="stylesheet">
<style>
:root{
  --red:#c4170c;
  --ink:#222222;
  --text:#555555;
  --muted:#888888;
  --line:#cccccc;
  --about-bg:#ececec;
  --skills-bg:#f2f3f5;
  --card:#ffffff;
  --service-card:#ededed;
  --dark:#26282c;
  --white:#ffffff;
}
*{margin:0;padding:0;box-sizing:border-box}
html,body{width:1200px;height:3441px;overflow:hidden}
body{position:relative;background:var(--white);font-family:"Lato",sans-serif;color:var(--text)}
.abs{position:absolute}
section,header,footer{position:absolute;left:0;width:1200px;overflow:hidden}
h1,h2,h3,h4,.mont{font-family:"Montserrat",sans-serif}

/* nav */
.site-header{top:0;height:55px;background:var(--white)}
.brand{left:225px;top:14px;display:flex;align-items:center;gap:6px;font-family:"Montserrat",sans-serif;font-weight:700;font-size:23px;color:#1d3a6b}
.brand-mark{width:10px;height:10px;background:var(--red)}
.nav{left:537px;top:25px;display:flex;gap:0;font-family:"Montserrat",sans-serif;font-weight:600;font-size:9.5px;color:#333}
.nav span{position:absolute;white-space:nowrap}
.nav .active{color:var(--red)}

/* hero */
.hero{top:55px;height:445px;background:var(--white)}
.hero-photo-left{left:0;top:0;width:608px;height:445px;background:linear-gradient(135deg,#dcdcda 0%,#c9c6c2 45%,#b9a99c 70%,#d8d6d4 100%)}
.hero-photo-right{left:850px;top:0;width:350px;height:445px;background:linear-gradient(90deg,#ffffff 0%,#d9d4d0 30%,#b8a79c 60%,#3a4152 100%)}
.hero-name{font-family:"Montserrat",sans-serif;font-weight:700;font-size:38px;top:118px}
.hero-left-text{right:628px;text-align:right}
.hero-right-text{left:664px}
.hero-role{font-family:"Montserrat",sans-serif;font-size:12px;color:#555;line-height:21.5px;top:186px}
.btn-about{top:267px;width:119px;height:32px;border-radius:5px;font-family:"Montserrat",sans-serif;font-weight:700;font-size:10px;display:flex;align-items:center;justify-content:center;gap:10px}
.btn-red{background:var(--red);color:var(--white)}
.btn-outline{border:1.5px solid #333;color:#222;background:var(--white);width:121px}

/* about */
.about{top:500px;height:593px;background:var(--about-bg)}
.about-divider{left:604px;top:56px;width:1px;height:494px;background:#d8d8d8}
.col{position:absolute;top:0;width:330px;height:593px}
.col-left{left:227px}
.col-right{left:659px}
.hello{top:76px;font-family:"Montserrat",sans-serif;font-size:12.5px;line-height:19px;color:#444}
.intro{top:121px;width:320px;font-size:8.6px;line-height:16px;color:#666}
.sub-title{font-family:"Montserrat",sans-serif;font-weight:500;font-size:19px}
.red{color:var(--red)}
.dark{color:#333}
.rule-long{height:1px;width:107px}
.rule-short{height:2px;width:58px}
.cv-card{left:1px;width:293px;height:100px;background:var(--card);box-shadow:0 2px 4px rgba(0,0,0,.18)}
.cv-card .corner{position:absolute;left:0;top:0;width:0;height:0;border-top:18px solid var(--red);border-right:18px solid transparent}
.col-right .cv-card .corner{border-top-color:#555}
.cv-date{position:absolute;left:18px;top:17px;font-size:8.5px;color:#444}
.cv-title{position:absolute;left:18px;top:31px;font-family:"Montserrat",sans-serif;font-weight:500;font-size:11.5px}
.cv-text{position:absolute;left:18px;top:52px;width:260px;font-size:8.6px;line-height:16px;color:#666}

/* skills */
.skills{top:1093px;height:688px;background:linear-gradient(160deg,#e8ebee 0%,#f4f5f7 35%,#f3f4f6 70%,#e9ecef 100%)}
.section-title{width:1200px;text-align:center;font-family:"Montserrat",sans-serif;font-weight:700}
.title-deco{left:553px;width:94px;height:10px}
.skill-head{font-family:"Montserrat",sans-serif;font-weight:500;font-size:20px;top:160px}
.skill-intro{top:204px;width:300px;font-size:8.6px;line-height:16px;color:#666}
.skill{position:absolute;width:294px;height:26px}
.skill-label{position:absolute;left:1px;top:0;font-size:10.5px;color:#555}
.skill-pct{position:absolute;top:1px;font-size:10.5px;color:#555;transform:translateX(-100%)}
.skill-track{position:absolute;left:0;top:19px;width:294px;height:3px;background:#c8c8c8}
.skill-fill{position:absolute;left:0;top:0;height:3px}
.fill-red{background:var(--red)}
.fill-dark{background:#222}

/* services */
.services{top:1781px;height:533px;background:linear-gradient(100deg,#3c4048 0%,#3a3633 35%,#4a3a33 65%,#3b3d42 100%)}
.services-shade{left:0;top:0;width:1200px;height:533px;background:rgba(20,22,28,.35)}
.service-card{width:231px;height:148px;background:var(--service-card);text-align:center}
.service-icon{position:absolute;left:98px;top:19px;width:35px;height:35px;border-radius:50%;background:var(--white);display:flex;align-items:center;justify-content:center}
.service-icon.filled{background:var(--red)}
.service-name{position:absolute;left:0;top:66px;width:231px;font-family:"Montserrat",sans-serif;font-weight:500;font-size:9.3px;color:#333}
.service-text{position:absolute;left:14px;top:88px;width:203px;font-size:8.6px;line-height:16px;color:#666}

/* works */
.works{top:2314px;height:363px;background:var(--white)}
.works-sub{top:89px;width:1200px;text-align:center;font-size:8.6px;line-height:15px;color:#4a6aa0}
.work{width:160px;top:148px}
.work-photo{width:160px;height:103px}
.work-title{margin-top:14px;font-family:"Montserrat",sans-serif;font-weight:600;font-size:8.6px;color:#222}
.work-text{margin-top:7px;font-size:8.6px;line-height:15px;color:#4a6aa0}

/* call to action */
.cta{top:2677px;height:209px;background:var(--red)}
.cta-title{left:297px;top:62px;font-family:"Montserrat",sans-serif;font-weight:700;font-size:22px;line-height:33px;color:var(--white)}
.cta-sub{left:297px;top:132px;font-family:"Montserrat",sans-serif;font-size:9.3px;color:var(--white)}
.btn-hire{left:798px;top:91px;width:112px;height:31px;border-radius:16px;background:var(--white);color:var(--red);font-family:"Montserrat",sans-serif;font-weight:700;font-size:12px;display:flex;align-items:center;justify-content:center}

/* contact */
.contact{top:2886px;height:508px;background:linear-gradient(120deg,#1f2125 0%,#2d3035 45%,#26292e 100%)}
.contact-item{left:235px;display:flex;align-items:center;gap:22px}
.contact-icon{width:40px;height:40px;border-radius:50%;background:var(--white);display:flex;align-items:center;justify-content:center}
.contact-text{font-family:"Montserrat",sans-serif;font-size:12px;line-height:19px;color:var(--white)}
.field{border:1px solid #8a8c90;background:transparent;font-size:8px;color:#aaa;padding:10px 12px}
.btn-send{left:484px;top:405px;width:137px;height:32px;border-radius:16px;background:var(--red);color:var(--white);font-family:"Montserrat",sans-serif;font-weight:600;font-size:11.5px;display:flex;align-items:center;justify-content:center}

/* footer */
.site-footer{top:3394px;height:47px;background:var(--white)}
.copyright{left:234px;top:19px;font-size:8px;color:#555}
.social{top:17px;width:12px;height:12px;border-radius:50%;background:#555}
</style>
</head>
<body>

<header class="site-header">
  <div class="abs brand"><span>Olven</span><span class="brand-mark"></span></div>
  <nav class="abs nav" style="left:0;top:25px">
    <span class="active" style="left:537px">HOME</span>
    <span style="left:592px">ABOUT</span>
    <span style="left:651px">SERVICE</span>
    <span style="left:715px">RESUME</span>
    <span style="left:779px">PORTFOLIO</span>
    <span style="left:857px">BLOG</span>
    <span style="left:909px">CONTACT US</span>
  </nav>
</header>

<section class="hero">
  <div class="abs hero-photo-left" role="img" aria-label="Portrait photo of Pieter, smiling man with glasses"></div>
  <div class="abs hero-photo-right" role="img" aria-label="Portrait photo of Marleen, woman with glasses"></div>

  <h1 class="abs hero-name hero-left-text red">Pieter</h1>
  <div class="abs hero-role hero-left-text">Advisor Veldmark<br>Advisor How &amp; knower<br>ppoipoipi opi poip l poi</div>
  <div class="abs btn-about btn-red" style="left:456px">ABOUT ME
    <svg width="8" height="6" viewBox="0 0 8 6"><path d="M1 1l3 3 3-3" fill="none" stroke="#fff" stroke-width="1.6"/></svg>
  </div>

  <h1 class="abs hero-name hero-right-text" style="color:#222">Marleen</h1>
  <div class="abs hero-role hero-right-text">Director Noordgas<br>jskldfjlkd&nbsp; lkjklj lkjklj ljlkj jkj kj klj<br>Netwijk</div>
  <div class="abs btn-about btn-outline" style="left:661px">ABOUT ME
    <svg width="8" height="6" viewBox="0 0 8 6"><path d="M1 1l3 3 3-3" fill="none" stroke="#222" stroke-width="1.6"/></svg>
  </div>
</section>

<section class="about">
  <div class="abs about-divider"></div>

  <div class="col col-left">
    <p class="abs hello">Hello I am Pieter, I am a Advisor Veldmark.<br>Brink Advocaten &amp; Notarissen Hollmer Audit</p>
    <p class="abs intro">loream isam Mauris scelerisque ut ipsum id vulputate. Nulla laoreet, ligula vel congue ultricies, nibh ipsum egestas nunc, id porta nibh nunc non felis. Vestibulum nibh urna, lobortis ut euismod.,</p>

    <h3 class="abs sub-title red" style="top:187px">Education</h3>
    <div class="abs rule-long" style="top:219px;background:#999"></div>
    <div class="abs rule-short" style="top:222px;left:27px;background:var(--red)"></div>
    <div class="abs cv-card" style="top:248px"><span class="corner"></span>
      <span class="cv-date">15 October 2015-27 March 2018</span>
      <span class="cv-title red">Kavra (RA)&nbsp; Atheneum B</span>
      <span class="cv-text">loream isam Mauris scelerisque ut ipsum id vulputate. Nulla laoreet, ligula vel congue ultricies,</span>
    </div>

    <h3 class="abs sub-title red" style="top:378px">Experience</h3>
    <div class="abs rule-long" style="top:410px;background:#999"></div>
    <div class="abs rule-short" style="top:413px;left:27px;background:var(--red)"></div>
    <div class="abs cv-card" style="top:439px"><span class="corner"></span>
      <span class="cv-date">15 October 2015-27 March 2018</span>
      <span class="cv-title red">Brink Advocaten &amp; Notarissen Hollmer Audit</span>
      <span class="cv-text">loream isam Mauris scelerisque ut ipsum id vulputate. Nulla laoreet, ligula vel congue ultricies,</span>
    </div>
  </div>

  <div class="col col-right">
    <p class="abs hello">Hello I am Marleen, I am a Director Noordgas.<br>Gasveld HVU</p>
    <p class="abs intro">loream isam Mauris scelerisque ut ipsum id vulputate. Nulla laoreet, ligula vel congue ultricies, nibh ipsum egestas nunc, id porta nibh nunc non felis. Vestibulum nibh urna, lobortis ut euismod.,</p>

    <h3 class="abs sub-title dark" style="top:187px">Education</h3>
    <div class="abs rule-long" style="top:219px;background:#999"></div>
    <div class="abs rule-short" style="top:222px;left:27px;background:var(--red)"></div>
    <div class="abs cv-card" style="top:248px"><span class="corner"></span>
      <span class="cv-date">15 October 2015-27 March 2018</span>
      <span class="cv-title dark">HVU&nbsp; Atheneum B</span>
      <span class="cv-text">loream isam Mauris scelerisque ut ipsum id vulputate. Nulla laoreet, ligula vel congue ultricies,</span>
    </div>

    <h3 class="abs sub-title dark" style="top:378px">Experience</h3>
    <div class="abs rule-long" style="top:410px;background:#999"></div>
    <div class="abs rule-short" style="top:413px;left:27px;background:var(--red)"></div>
    <div class="abs cv-card" style="top:439px"><span class="corner"></span>
      <span class="cv-date">15 October 2015-27 March 2018</span>
      <span class="cv-title dark">Gasveld HVU</span>
      <span class="cv-text">loream isam Mauris scelerisque ut ipsum id vulputate. Nulla laoreet, ligula vel congue ultricies,</span>
    </div>
  </div>
</section>

<section class="skills" role="img" aria-label="Soft background photo of a desk with keyboard and plant">
  <h2 class="abs section-title" style="top:63px;font-size:24px;color:#444">OUR SKILLS</h2>
  <svg class="abs title-deco" style="top:92px" viewBox="0 0 94 10">
    <line x1="6" y1="5" x2="88" y2="5" stroke="#555" stroke-width="1"/>
    <line x1="20" y1="8" x2="74" y2="8" stroke="#555" stroke-width="1"/>
    <circle cx="4" cy="5" r="3" fill="none" stroke="#555"/><circle cx="90" cy="5" r="3" fill="none" stroke="#555"/>
  </svg>

  <!-- left person -->
  <h3 class="abs skill-head red" style="left:232px">Pieter Skills</h3>
  <div class="abs rule-short" style="left:232px;top:191px;width:68px;height:1px;background:var(--red)"></div>
  <p class="abs skill-intro" style="left:234px">loream isam Mauris scelerisque ut ipsum id vulputate. Nulla laoreet, ligula vel congue ultricies, nibh ipsum.</p>

  <div class="skill" style="left:234px;top:250px"><span class="skill-label">Annual reporting</span><span class="skill-pct" style="left:252px">90%</span><div class="skill-track"><div class="skill-fill fill-red" style="width:90%"></div></div></div>
  <div class="skill" style="left:234px;top:305px"><span class="skill-label">Financial monthly reporting</span><span class="skill-pct" style="left:208px">72%</span><div class="skill-track"><div class="skill-fill fill-red" style="width:72%"></div></div></div>
  <div class="skill" style="left:234px;top:360px"><span class="skill-label">Accounting</span><span class="skill-pct" style="left:294px">100%</span><div class="skill-track"><div class="skill-fill fill-red" style="width:100%"></div></div></div>
  <div class="skill" style="left:234px;top:415px"><span class="skill-label">Financial management</span><span class="skill-pct" style="left:208px">70%</span><div class="skill-track"><div class="skill-fill fill-red" style="width:70%"></div></div></div>
  <div class="skill" style="left:234px;top:466px"><span class="skill-label">Project management</span><span class="skill-pct" style="left:208px">70%</span><div class="skill-track"><div class="skill-fill fill-red" style="width:70%"></div></div></div>
  <div class="skill" style="left:234px;top:526px"><span class="skill-label">Team player</span><span class="skill-pct" style="left:252px">90%</span><div class="skill-track"><div class="skill-fill fill-red" style="width:90%"></div></div></div>
  <div class="skill" style="left:234px;top:585px"><span class="skill-label">Trouble shooter</span><span class="skill-pct" style="left:252px">90%</span><div class="skill-track"><div class="skill-fill fill-red" style="width:90%"></div></div></div>

  <!-- right person -->
  <h3 class="abs skill-head dark" style="left:651px">Marleen Skills</h3>
  <div class="abs rule-short" style="left:651px;top:191px;width:68px;height:1px;background:#333"></div>
  <p class="abs skill-intro" style="left:653px">loream isam Mauris scelerisque ut ipsum id vulputate. Nulla laoreet, ligula vel congue ultricies, nibh ipsum.</p>

  <div class="skill" style="left:653px;top:250px"><span class="skill-label">General management</span><span class="skill-pct" style="left:252px">90%</span><div class="skill-track"><div class="skill-fill fill-dark" style="width:90%"></div></div></div>
  <div class="skill" style="left:653px;top:305px"><span class="skill-label">Energy knowledge</span><span class="skill-pct" style="left:208px">72%</span><div class="skill-track"><div class="skill-fill fill-dark" style="width:72%"></div></div></div>
  <div class="skill" style="left:653px;top:360px"><span class="skill-label">Gas knowledge</span><span class="skill-pct" style="left:294px">100%</span><div class="skill-track"><div class="skill-fill fill-dark" style="width:100%"></div></div></div>
  <div class="skill" style="left:653px;top:415px"><span class="skill-label">People management</span><span class="skill-pct" style="left:208px">70%</span><div class="skill-track"><div class="skill-fill fill-dark" style="width:70%"></div></div></div>
  <div class="skill" style="left:653px;top:466px"><span class="skill-label">Project management</span><span class="skill-pct" style="left:208px">70%</span><div class="skill-track"><div class="skill-fill fill-dark" style="width:70%"></div></div></div>
  <div class="skill" style="left:653px;top:526px"><span class="skill-label">Team player</span><span class="skill-pct" style="left:252px">90%</span><div class="skill-track"><div class="skill-fill fill-dark" style="width:90%"></div></div></div>
  <div class="skill" style="left:653px;top:585px"><span class="skill-label">Trouble shooter</span><span class="skill-pct" style="left:252px">90%</span><div class="skill-track"><div class="skill-fill fill-dark" style="width:90%"></div></div></div>
</section>

<section class="services">
  <div class="abs services-shade" role="img" aria-label="Dark background photo of a brick office building with trees"></div>
  <h2 class="abs section-title" style="top:63px;font-size:23px;color:#fff">We Provide Best Services</h2>
  <svg class="abs title-deco" style="top:98px" viewBox="0 0 94 10">
    <line x1="6" y1="5" x2="88" y2="5" stroke="#fff" stroke-width="1"/>
    <line x1="20" y1="8" x2="74" y2="8" stroke="#c4170c" stroke-width="1"/>
    <circle cx="4" cy="5" r="3" fill="none" stroke="#c4170c"/><circle cx="90" cy="5" r="3" fill="none" stroke="#c4170c"/>
  </svg>

  <div class="abs service-card" style="left:234px;top:148px">
    <div class="service-icon"><svg width="14" height="16" viewBox="0 0 14 16"><rect x="1" y="1" width="12" height="14" rx="1" fill="none" stroke="#c4170c"/><rect x="3" y="3" width="8" height="3" fill="#c4170c"/><path d="M3 9h2M6 9h2M9 9h2M3 12h2M6 12h2M9 12h2" stroke="#c4170c"/></svg></div>
    <div class="service-name">FINANCIAL PLANNER</div>
    <p class="service-text">loream isam Mauris scelerisque ut ipsum id Nulla laoreet, ligula vel congue ultricies, nibh ipsum egestas nunc, id porta</p>
  </div>
  <div class="abs service-card" style="left:484px;top:148px">
    <div class="service-icon filled"><svg width="16" height="14" viewBox="0 0 16 14"><rect x="1" y="3" width="14" height="10" rx="2" fill="none" stroke="#fff"/><path d="M3 3l7-2 1 2" fill="none" stroke="#fff"/><circle cx="12" cy="8" r="1.2" fill="#fff"/></svg></div>
    <div class="service-name">MORTGAGE ADVISOR</div>
    <p class="service-text">loream isam Mauris scelerisque ut ipsum id Nulla laoreet, ligula vel congue ultricies, nibh ipsum egestas nunc, id porta</p>
  </div>
  <div class="abs service-card" style="left:733px;top:148px">
    <div class="service-icon"><svg width="18" height="14" viewBox="0 0 18 14"><ellipse cx="9" cy="8" rx="7" ry="5" fill="none" stroke="#c4170c"/><circle cx="9" cy="3" r="2" fill="none" stroke="#c4170c"/></svg></div>
    <div class="service-name">INVESTMENT ADVISOR</div>
    <p class="service-text">loream isam Mauris scelerisque ut ipsum id Nulla laoreet, ligula vel congue ultricies, nibh ipsum egestas nunc, id porta</p>
  </div>
  <div class="abs service-card" style="left:234px;top:315px">
    <div class="service-icon"><svg width="14" height="16" viewBox="0 0 14 16"><path d="M4 1h6l-2 3h-2z" fill="none" stroke="#c4170c"/><circle cx="7" cy="10" r="5" fill="none" stroke="#c4170c"/><path d="M7 7v6" stroke="#c4170c"/></svg></div>
    <div class="service-name">PENSION ADVISOR</div>
    <p class="service-text">loream isam Mauris scelerisque ut ipsum id Nulla laoreet, ligula vel congue ultricies, nibh ipsum egestas nunc, id porta</p>
  </div>
  <div class="abs service-card" style="left:484px;top:315px">
    <div class="service-icon"><svg width="16" height="14" viewBox="0 0 16 14"><rect x="1" y="1" width="14" height="12" fill="none" stroke="#c4170c"/><path d="M4 5h8M4 8h8M4 11h5" stroke="#c4170c"/></svg></div>
    <div class="service-name">TRUSTED FINANCIAL ADVICE</div>
    <p class="service-text">loream isam Mauris scelerisque ut ipsum id Nulla laoreet, ligula vel congue ultricies, nibh ipsum egestas nunc, id porta</p>
  </div>
  <div class="abs service-card" style="left:733px;top:315px">
    <div class="service-icon"><svg width="18" height="12" viewBox="0 0 18 12"><path d="M1 4l4-3 4 3 4-3 4 3M3 6l6 5 6-5" fill="none" stroke="#c4170c"/></svg></div>
    <div class="service-name">RELIABLE PARTNER</div>
    <p class="service-text">loream isam Mauris scelerisque ut ipsum id Nulla laoreet, ligula vel congue ultricies, nibh ipsum egestas nunc, id porta</p>
  </div>
</section>

<section class="works">
  <h2 class="abs section-title" style="top:50px;font-size:23px;color:#111">OUR WORKS</h2>
  <p class="abs works-sub">Lorem ipsum dolor sit amet, consectetur adipisicing elit, sed do eiusmod tempor incidid-<br>unt ut labore et dolore magna aliqua</p>

  <div class="abs work" style="left:228px">
    <div class="work-photo" role="img" aria-label="Photo of business people reviewing a tablet" style="background:linear-gradient(135deg,#8aa0b8,#2d3644 60%,#5c6a7c)"></div>
    <div class="work-title">DIRECTOR GASVELD</div>
    <p class="work-text">Lorem ipsum dolor sit amet, consecte-<br>tur adipisicing elit, sed do eiusmod</p>
  </div>
  <div class="abs work" style="left:429px">
    <div class="work-photo" role="img" aria-label="Photo of two colleagues smiling at an office desk" style="background:linear-gradient(135deg,#e6ecf2,#9fb2c8 50%,#dfe6ee)"></div>
    <div class="work-title">ADVISOR GAS</div>
    <p class="work-text">Lorem ipsum dolor sit amet, consecte-<br>tur adipisicing elit, sed do eiusmod</p>
  </div>
  <div class="abs work" style="left:615px">
    <div class="work-photo" role="img" aria-label="Photo of hands over financial charts on a table" style="background:linear-gradient(135deg,#4a5260,#cfd6e0 45%,#8a9ab0)"></div>
    <div class="work-title">ADVISOR DELTA GREEN</div>
    <p class="work-text">Lorem ipsum dolor sit amet, consecte-<br>tur adipisicing elit, sed do eiusmod</p>
  </div>
  <div class="abs work" style="left:815px">
    <div class="work-photo" role="img" aria-label="Photo of a business handshake" style="background:linear-gradient(135deg,#dfe4ea,#3a4658 55%,#7c8da4)"></div>
    <div class="work-title">OIPOIP O KKLJK</div>
    <p class="work-text">Lorem ipsum dolor sit amet, consecte-<br>tur adipisicing elit, sed do eiusmod</p>
  </div>
</section>

<section class="cta">
  <h2 class="abs cta-title">We are availabe<br>for&nbsp; Financial and Accounting services.</h2>
  <p class="abs cta-sub">Tell me about your&nbsp; project story and project brief</p>
  <div class="abs btn-hire">HIRE US</div>
</section>

<section class="contact" role="img" aria-label="Dark background photo of a hand over financial charts">
  <h2 class="abs section-title" style="top:62px;font-size:23px;color:#fff">Contact Us</h2>
  <svg class="abs title-deco" style="top:94px" viewBox="0 0 94 10">
    <line x1="6" y1="5" x2="88" y2="5" stroke="#fff" stroke-width="1"/>
    <line x1="20" y1="8" x2="74" y2="8" stroke="#c4170c" stroke-width="1"/>
    <circle cx="4" cy="5" r="3" fill="none" stroke="#c4170c"/><circle cx="90" cy="5" r="3" fill="none" stroke="#c4170c"/>
  </svg>

  <div class="abs contact-item" style="top:168px">
    <div class="contact-icon"><svg width="16" height="12" viewBox="0 0 16 12"><rect width="16" height="12" rx="2" fill="#c4170c"/><path d="M1 1.5l7 5 7-5" fill="none" stroke="#fff" stroke-width="1.3"/></svg></div>
    <div class="contact-text">contact@olvenmail.com<br>Your email name@olvenmail.com</div>
  </div>
  <div class="abs contact-item" style="top:243px">
    <div class="contact-icon"><svg width="14" height="14" viewBox="0 0 24 24"><path d="M6.6 10.8a15 15 0 006.6 6.6l2.2-2.2c.3-.3.7-.4 1-.2 1.1.4 2.3.6 3.6.6.6 0 1 .4 1 1V20c0 .6-.4 1-1 1A17 17 0 013 4c0-.6.4-1 1-1h3.5c.6 0 1 .4 1 1 0 1.3.2 2.5.6 3.6.1.3 0 .7-.2 1z" fill="#c4170c"/></svg></div>
    <div class="contact-text">0031501234567<br>0031509876543</div>
  </div>
  <div class="abs contact-item" style="top:318px">
    <div class="contact-icon"><svg width="12" height="16" viewBox="0 0 12 16"><path d="M6 0a6 6 0 00-6 6c0 4.5 6 10 6 10s6-5.5 6-10a6 6 0 00-6-6z" fill="#c4170c"/><circle cx="6" cy="6" r="2.2" fill="#fff"/></svg></div>
    <div class="contact-text">Groningen 9711, Veldstraat<br>Oosterpoort, Netherlands</div>
  </div>

  <div class="abs field" style="left:484px;top:168px;width:231px;height:30px">Your Name.......</div>
  <div class="abs field" style="left:733px;top:168px;width:232px;height:30px">Email Address.....</div>
  <div class="abs field" style="left:484px;top:217px;width:481px;height:157px">Your Messages.....</div>
  <div class="abs btn-send">SEND MESSAGES</div>
</section>

<footer class="site-footer">
  <p class="abs copyright">copyright @ OLVEN BV&nbsp; 2018. All rights reserved</p>
  <span class="abs social" style="left:804px" aria-label="Social profile"></span>
  <span class="abs social" style="left:841px" aria-label="Social profile"></span>
  <span class="abs social" style="left:878px;background:var(--red)" aria-label="Social profile"></span>
  <span class="abs social" style="left:916px" aria-label="Social profile"></span>
  <span class="abs social" style="left:953px" aria-label="Social profile"></span>
</footer>

</body>
</html>
```